Business Card
Larkframe, LLC
Professional
Omar Pettis
Founder and CEO
412 Birchwell Rd
Fernhollow, VT 05134
omar.pettis@larkframe.com
www.larkframe.com
I am open on the font choice. A different font may be used if it works visually.
Nothing
Illustrator file of our Corporate Logo

```html
<!DOCTYPE html>
<html lang="en">
<head>
<meta charset="utf-8">
<title>Larkframe Stationery</title>
<link rel="stylesheet" href="https://fonts.googleapis.com/css2?family=Montserrat:wght@400;600;700&display=swap">
<style>
  :root {
    --bg: #e9e9eb;
    --paper: #ffffff;
    --ink: #2a2f3a;
    --muted: #6d7480;
    --brand-blue: #1f4f9c;
    --brand-deep: #0f2f6a;
    --brand-sky: #3f86d6;
    --brand-green: #7cc243;
    --brand-lime: #a8d85a;
    --rule: #d7dbe2;
  }
  * { box-sizing: border-box; margin: 0; padding: 0; }
  html, body { width: 1200px; height: 632px; overflow: hidden; }
  body {
    position: relative;
    background: var(--bg);
    font-family: "Montserrat", sans-serif;
    color: var(--ink);
  }
  .piece { position: absolute; background: var(--paper); box-shadow: 0 3px 10px rgba(0,0,0,.18); overflow: hidden; }

  /* brand lockup */
  .brand { display: flex; align-items: center; gap: 5px; }
  .brand-dot { border-radius: 50%; background: var(--brand-blue); flex: none; }
  .brand-name { font-weight: 700; color: var(--brand-blue); letter-spacing: -.3px; line-height: 1; white-space: nowrap; }
  .brand-tag { font-size: 4px; color: var(--muted); margin-top: 2px; letter-spacing: .2px; white-space: nowrap; }
  .on-dark .brand-name, .on-dark .brand-tag { color: #fff; }
  .on-dark .brand-dot { background: #fff; }

  /* business cards */
  .card { left: 125px; width: 122px; height: 102px; border-radius: 4px; }
  .card-front { top: 72px; }
  .card-front .brand { position: absolute; left: 8px; top: 9px; }
  .card-front .brand-dot { width: 11px; height: 11px; }
  .card-front .brand-name { font-size: 10px; }
  .card-person { position: absolute; left: 8px; top: 44px; font-size: 4px; line-height: 1.5; color: var(--muted); }
  .card-person strong { display: block; font-size: 5px; color: var(--brand-blue); }
  .card-contact { position: absolute; left: 62px; top: 44px; font-size: 3.6px; line-height: 1.6; color: var(--muted); white-space: nowrap; }
  .card-bar { position: absolute; left: 0; right: 0; bottom: 0; height: 11px; background: linear-gradient(90deg, var(--brand-deep), var(--brand-sky)); color: #fff; font-size: 4px; letter-spacing: 1.2px; text-align: center; line-height: 11px; }

  .card-center { display: flex; align-items: center; justify-content: center; }
  .card-center .brand-dot { width: 13px; height: 13px; }
  .card-center .brand-name { font-size: 12px; }
  .card-white { top: 199px; }
  .card-white svg { position: absolute; left: 0; bottom: 0; }
  .card-blue { top: 328px; background: radial-gradient(circle at 55% 45%, var(--brand-sky), var(--brand-deep) 75%); }
  .card-green { top: 454px; background: radial-gradient(circle at 55% 45%, var(--brand-lime), #3f8f2a 80%); }

  /* letterhead */
  .letterhead { left: 348px; top: 67px; width: 377px; height: 492px; }
  .letterhead .brand { position: absolute; left: 24px; top: 24px; }
  .letterhead .brand-dot { width: 20px; height: 20px; }
  .letterhead .brand-name { font-size: 19px; }
  .letterhead .brand-tag { font-size: 5px; }
  .letterhead-address { position: absolute; left: 24px; top: 58px; font-size: 5px; line-height: 1.7; color: var(--muted); }
  .letterhead-mark { position: absolute; left: 73px; top: 150px; width: 230px; height: 230px; border-radius: 50%; background: radial-gradient(circle, #f3f6fb, #e3e9f3); }
  .letterhead-footer { position: absolute; left: 0; right: 0; bottom: 0; height: 16px; background: linear-gradient(90deg, var(--brand-deep), var(--brand-sky)); color: #fff; font-size: 6px; letter-spacing: 3px; text-align: center; line-height: 16px; }

  /* envelopes */
  .envelope svg { position: absolute; left: 0; top: 0; }
  .env-green { left: 739px; top: 67px; width: 319px; height: 185px; }
  .env-white { left: 830px; top: 175px; width: 300px; height: 130px; }
  .env-blue { left: 739px; top: 281px; width: 307px; height: 182px; }
  .env-front { left: 799px; top: 403px; width: 343px; height: 159px; }
  .env-front .brand { position: absolute; left: 18px; top: 28px; }
  .env-front .brand-dot { width: 15px; height: 15px; }
  .env-front .brand-name { font-size: 15px; }
  .env-front-address { position: absolute; left: 18px; top: 56px; font-size: 5px; line-height: 1.6; color: var(--muted); }
  .env-front-bar { position: absolute; left: 0; right: 0; bottom: 0; height: 9px; background: linear-gradient(90deg, var(--brand-deep), var(--brand-sky)); color: #fff; font-size: 4px; letter-spacing: 2px; text-align: center; line-height: 9px; }
</style>
</head>
<body>

  <section class="piece card card-front">
    <div class="brand">
      <span class="brand-dot"></span>
      <div><div class="brand-name">Larkframe</div><div class="brand-tag">Video Studio • Story Production</div></div>
    </div>
    <div class="card-person"><strong>Omar Pettis</strong>Founder and CEO</div>
    <div class="card-contact">
      412 Birchwell Rd<br>Fernhollow, VT 05134<br>T (555) 010-0142<br>omar.pettis@larkframe.com
    </div>
    <div class="card-bar">www.larkframe.com</div>
  </section>

  <section class="piece card card-white card-center">
    <div class="brand">
      <span class="brand-dot"></span>
      <div><div class="brand-name">Larkframe</div><div class="brand-tag">Video Studio • Story Production</div></div>
    </div>
    <svg width="122" height="20" viewBox="0 0 122 20" aria-hidden="true">
      <path d="M0 12 Q61 2 122 10 V20 H0 Z" fill="var(--brand-lime)"/>
      <path d="M0 16 Q61 8 122 14 V20 H0 Z" fill="var(--brand-blue)"/>
    </svg>
  </section>

  <section class="piece card card-blue card-center on-dark">
    <div class="brand">
      <span class="brand-dot"></span>
      <div><div class="brand-name">Larkframe</div><div class="brand-tag">Video Studio • Story Production</div></div>
    </div>
  </section>

  <section class="piece card card-green card-center on-dark">
    <div class="brand">
      <span class="brand-dot"></span>
      <div><div class="brand-name">Larkframe</div><div class="brand-tag">Video Studio • Story Production</div></div>
    </div>
  </section>

  <section class="piece letterhead">
    <div class="brand">
      <span class="brand-dot"></span>
      <div><div class="brand-name">Larkframe</div><div class="brand-tag">Video Studio • Story Production</div></div>
    </div>
    <div class="letterhead-address">
      412 Birchwell Rd, Fernhollow, VT 05134<br>
      T (555) 010-0142 &nbsp;|&nbsp; E omar.pettis@larkframe.com
    </div>
    <div class="letterhead-mark"></div>
    <div class="letterhead-footer">www.larkframe.com</div>
  </section>

  <section class="piece envelope env-green">
    <svg width="319" height="185" viewBox="0 0 319 185" aria-hidden="true">
      <defs>
        <linearGradient id="flapGreen" x1="0" y1="0" x2="0" y2="1">
          <stop offset="0" stop-color="var(--brand-lime)"/>
          <stop offset="1" stop-color="#3f8f2a"/>
        </linearGradient>
      </defs>
      <path d="M0 185 L160 92 L319 185" fill="none" stroke="var(--rule)"/>
      <path d="M0 0 H319 L167 100 Q160 105 152 100 Z" fill="url(#flapGreen)"/>
      <circle cx="160" cy="94" r="8" fill="var(--brand-blue)" stroke="#fff" stroke-width="2"/>
    </svg>
  </section>

  <section class="piece envelope env-white">
    <svg width="300" height="130" viewBox="0 0 300 130" aria-hidden="true">
      <path d="M0 130 L150 66 L300 130" fill="none" stroke="var(--rule)"/>
      <path d="M0 0 H300 L156 70 Q150 74 144 70 Z" fill="#f7f8fa" stroke="var(--rule)"/>
      <circle cx="150" cy="66" r="7" fill="var(--brand-blue)" stroke="#fff" stroke-width="2"/>
    </svg>
  </section>

  <section class="piece envelope env-blue">
    <svg width="307" height="182" viewBox="0 0 307 182" aria-hidden="true">
      <defs>
        <linearGradient id="flapBlue" x1="0" y1="0" x2="0" y2="1">
          <stop offset="0" stop-color="var(--brand-sky)"/>
          <stop offset="1" stop-color="var(--brand-deep)"/>
        </linearGradient>
      </defs>
      <path d="M0 182 L154 94 L307 182" fill="none" stroke="var(--rule)"/>
      <path d="M0 0 H307 L161 94 Q154 99 146 94 Z" fill="url(#flapBlue)"/>
      <circle cx="154" cy="88" r="8" fill="var(--brand-lime)" stroke="#fff" stroke-width="2"/>
    </svg>
  </section>

  <section class="piece envelope env-front">
    <div class="brand">
      <span class="brand-dot"></span>
      <div><div class="brand-name">Larkframe</div><div class="brand-tag">Video Studio • Story Production</div></div>
    </div>
    <div class="env-front-address">412 Birchwell Rd<br>Fernhollow, VT 05134</div>
    <div class="env-front-bar">www.larkframe.com</div>
  </section>

</body>
</html>
```